Business Postcard Mailer - 2 sided - 6 x 10.5 inches

We will be purchasing multiple designs through this project. We need a postcard mailer for a residential painting business. The final design needs to have the special 15% Off, contact information, company logo, stamp indicia, and list of services. I will provide past examples and any additional logos. Company colors are #34482E and #4A1717. Old samples are provided. Final flat size should be 6 x 10.5 inches. And we will need a return address in the upper left-hand corner of the backside. QMRB Layout Guidelines are attached. 4389 Juniper Ave #7, Waukesha, WI 53947.
Updates

I just guaranteed the project and will be expecting more entries. We will also be purchasing additional designs (4-5) so we want to ensure a good variety.

Target Market(s)

Homeowners

Industry/Entity Type

Painting

Font styles to use
Sans Serif

Requirements
Must have
• Logo and brand colors
Nice to have
• Call to action - Book your free estimate at www.BrightCoatCrew.example or Call now 262-555-0147.

```html
<!DOCTYPE html>
<html lang="en">
<head>
<meta charset="utf-8">
<title>Bright Coat Crew – Postcard Mailer</title>
<link href="https://fonts.googleapis.com/css2?family=Arimo:wght@400;700&display=swap" rel="stylesheet">
<style>
  :root {
    --green: #34482E;
    --maroon: #4A1717;
    --band-light: #e8e9ea;
    --band-dark: #3d3d3f;
    --panel-grey: #e6e6e7;
    --white: #ffffff;
    --badge: #b9bcbf;
  }
  * { box-sizing: border-box; margin: 0; padding: 0; }
  html, body { width: 1200px; height: 398px; overflow: hidden; }
  body {
    font-family: "Arimo", Arial, sans-serif;
    background: linear-gradient(to bottom, var(--band-light) 0 276px, var(--band-dark) 276px 100%);
    position: relative;
  }
  .card {
    position: absolute; top: 38px; width: 558px; height: 320px;
    background: var(--white); overflow: hidden;
  }
  .card--front { left: 32px; }
  .card--back { left: 611px; width: 557px; }
  .abs { position: absolute; }

  /* Front */
  .brand {
    left: 18px; top: 36px; width: 200px; display: flex; align-items: center; gap: 9px;
    color: var(--green); font-weight: 700; font-size: 30px; line-height: 1.05; letter-spacing: -0.5px;
  }
  .brand-mark { width: 16px; height: 16px; background: var(--maroon); flex: none; }
  .front-phone {
    left: 228px; top: 28px; color: var(--maroon); font-weight: 700; font-size: 50px; line-height: 1; letter-spacing: -0.5px;
    white-space: nowrap;
  }
  .front-url {
    left: 230px; top: 78px; color: var(--green); font-weight: 700; font-size: 19px; line-height: 1; white-space: nowrap;
  }
  .services-panel {
    left: 0; top: 120px; width: 210px; height: 200px; background: var(--green);
  }
  .services-panel h2 {
    position: absolute; left: 18px; top: 8px; color: var(--white); font-size: 18px; font-weight: 700;
  }
  .service-list { list-style: none; position: absolute; left: 18px; top: 36px; }
  .service-list li {
    display: flex; align-items: center; gap: 6px; height: 19.5px;
    color: var(--white); font-size: 15px; font-weight: 700; white-space: nowrap;
  }
  .service-list svg { width: 11px; height: 11px; flex: none; }
  .specials {
    left: 6px; top: 254px; width: 200px; height: 60px; background: var(--white);
    display: flex; justify-content: space-between; align-items: center; padding: 0 6px;
  }
  .special { color: var(--maroon); font-weight: 700; }
  .special-row { display: flex; align-items: center; line-height: 1; }
  .special-label { font-size: 9px; text-align: left; line-height: 1.05; }
  .special-num { font-size: 27px; letter-spacing: -1px; }
  .special-off { font-size: 8px; line-height: 1.05; }
  .special-note { font-size: 5px; margin-top: 2px; white-space: nowrap; }
  .photo { position: absolute; }
  .photo--house-a { left: 214px; top: 104px; width: 115px; height: 190px;
    background: linear-gradient(to bottom, #6fa6d8 0%, #a9c9e6 38%, #5f7689 55%, #7c8e9b 70%, #5f9a3f 85%, #4c8431 100%); }
  .photo--house-b { left: 334px; top: 104px; width: 104px; height: 190px;
    background: linear-gradient(to bottom, #7db0dd 0%, #b7d3ea 35%, #5d6f7c 55%, #7a8b96 72%, #5e9a40 86%, #4b8230 100%); }
  .photo--carpentry { left: 442px; top: 104px; width: 100px; height: 94px;
    background: linear-gradient(135deg, #c98f5b 0%, #a8673a 50%, #d9c2a8 100%); }
  .photo--drywall { left: 442px; top: 200px; width: 100px; height: 94px;
    background: linear-gradient(135deg, #e3e3e1 0%, #cfcfcc 55%, #b06a4c 100%); }

  /* Back */
  .promise {
    left: 26px; top: 19px; width: 370px; color: var(--maroon); font-weight: 700; font-size: 11.5px; line-height: 1.3;
  }
  .grey-band { left: 0; top: 56px; width: 414px; height: 146px; background: var(--panel-grey); }
  .back-title { left: 27px; top: 77px; color: var(--green); font-weight: 700; font-size: 19px; letter-spacing: 0.3px; }
  .back-list { left: 27px; top: 104px; position: absolute; list-style: none; }
  .back-list li {
    display: flex; align-items: center; gap: 8px; height: 19.2px;
    color: var(--maroon); font-size: 15.5px; font-weight: 700; white-space: nowrap;
  }
  .back-list svg { width: 11px; height: 11px; flex: none; color: var(--maroon); }
  .photo--before { left: 217px; top: 71px; width: 76px; height: 62px; border: 2px solid var(--white);
    background: linear-gradient(to bottom, #c6d4de 0%, #e2e4e1 45%, #bfc2bb 75%, #7f9a61 100%); }
  .photo--after { left: 217px; top: 134px; width: 76px; height: 62px; border: 2px solid var(--white);
    background: linear-gradient(to bottom, #c9d7e2 0%, #5f6d80 45%, #4f5c6e 75%, #7f9a61 100%); }
  .badge { position: absolute; background: var(--badge); }
  .badge--rating { left: 330px; top: 85px; width: 40px; height: 48px; border-radius: 3px; }
  .badge--assoc-a { left: 306px; top: 148px; width: 22px; height: 18px; }
  .badge--assoc-b { left: 332px; top: 146px; width: 54px; height: 22px; border-radius: 3px; }
  .badge--assoc-c { left: 306px; top: 172px; width: 22px; height: 18px; }
  .badge--assoc-d { left: 334px; top: 172px; width: 28px; height: 18px; }
  .badge--assoc-e { left: 366px; top: 172px; width: 24px; height: 18px; }

  .mail-column { left: 414px; top: 0; width: 143px; height: 202px; background: var(--green); }
  .return-address {
    position: absolute; left: 14px; top: 20px; color: var(--white); font-weight: 700; font-size: 10.5px; line-height: 1.3;
  }
  .indicia {
    position: absolute; left: 79px; top: 17px; width: 48px; height: 50px; background: var(--white);
    border: 1px solid var(--white); outline: 1px solid #333; outline-offset: -4px;
    display: flex; flex-direction: column; align-items: center; justify-content: center;
    font-size: 5.4px; line-height: 1.15; text-align: center; color: #111;
  }
  .indicia strong { font-size: 7px; margin: 1px 0; }
  .offer {
    position: absolute; left: 13px; width: 116px; background: var(--white); border-radius: 6px;
    text-align: center; color: var(--green);
  }
  .offer--fall { top: 82px; height: 50px; }
  .offer--winter { top: 142px; height: 52px; }
  .offer-amount { font-size: 21px; font-weight: 700; font-style: italic; line-height: 1; margin-top: 6px; }
  .offer-name { font-size: 10px; line-height: 1.1; }
  .offer-note { font-size: 4.5px; line-height: 1.2; }

  .cta-title { left: 27px; top: 218px; color: var(--green); font-weight: 700; font-size: 18.5px; }
  .contact { left: 27px; top: 242px; color: var(--maroon); font-weight: 700; font-size: 15px; line-height: 20px; white-space: nowrap; }
  .consult {
    left: 262px; top: 250px; width: 113px; height: 50px; background: var(--green);
    border: 1px solid #c9d3c3; border-radius: 4px; text-align: center; color: var(--white);
  }
  .consult-free { font-size: 19px; font-weight: 700; font-style: italic; line-height: 1; margin-top: 5px; }
  .consult-name { font-size: 8.5px; line-height: 1.1; }
  .consult-note { font-size: 4.6px; line-height: 1.2; }
</style>
</head>
<body>

<svg width="0" height="0" style="position:absolute" aria-hidden="true">
  <defs>
    <symbol id="tick-box" viewBox="0 0 12 12">
      <rect x="0.75" y="0.75" width="10.5" height="10.5" fill="none" stroke="currentColor" stroke-width="1.3"/>
      <path d="M2.6 6.2 L5 8.6 L9.6 3.2" fill="none" stroke="currentColor" stroke-width="1.6"/>
    </symbol>
  </defs>
</svg>

<section class="card card--front" aria-label="Postcard front">
  <div class="abs brand"><span class="brand-mark"></span><span>Bright Coat<br>Crew</span></div>
  <div class="abs front-phone">262-555-0147</div>
  <div class="abs front-url">www.BrightCoatCrew.example</div>

  <div class="abs services-panel">
    <h2>Free Estimates</h2>
    <ul class="service-list">
      <li><svg><use href="#tick-box"/></svg>Interior Painting</li>
      <li><svg><use href="#tick-box"/></svg>Exterior Painting</li>
      <li><svg><use href="#tick-box"/></svg>Carpentry Services</li>
      <li><svg><use href="#tick-box"/></svg>Drywall Repair</li>
      <li><svg><use href="#tick-box"/></svg>Color Consultations</li>
    </ul>
  </div>

  <div class="abs specials">
    <div class="special">
      <div class="special-row">
        <span class="special-label">FALL<br>Special</span>
        <span class="special-num">15</span>
        <span class="special-off">%<br>OFF</span>
      </div>
      <div class="special-note">while openings are still available</div>
    </div>
    <div class="special">
      <div class="special-row">
        <span class="special-label">WINTER<br>Special</span>
        <span class="special-num">25</span>
        <span class="special-off">%<br>OFF</span>
      </div>
      <div class="special-note">December - February, Interior Only</div>
    </div>
  </div>

  <div class="photo photo--house-a" role="img" aria-label="Photo of a freshly painted two-storey blue-grey house with lawn"></div>
  <div class="photo photo--house-b" role="img" aria-label="Photo of the same house from a second angle"></div>
  <div class="photo photo--carpentry" role="img" aria-label="Photo of hands hammering on wooden boards"></div>
  <div class="photo photo--drywall" role="img" aria-label="Photo of a hand smoothing drywall compound with a putty knife"></div>
</section>

<section class="card card--back" aria-label="Postcard back">
  <p class="abs promise">We cater the size of the crew to the size of the job and work full continuous days until the project is complete.</p>

  <div class="abs grey-band"></div>
  <div class="abs back-title">FREE ESTIMATES</div>
  <ul class="back-list">
    <li><svg><use href="#tick-box"/></svg>Interior Painting</li>
    <li><svg><use href="#tick-box"/></svg>Exterior Painting</li>
    <li><svg><use href="#tick-box"/></svg>Carpentry Services</li>
    <li><svg><use href="#tick-box"/></svg>Drywall Repair</li>
    <li><svg><use href="#tick-box"/></svg>Color Consultations</li>
  </ul>
  <div class="abs photo--before" role="img" aria-label="Before photo of a house with weathered white paint"></div>
  <div class="abs photo--after" role="img" aria-label="After photo of the same house painted dark blue-grey"></div>

  <div class="badge badge--rating" role="img" aria-label="Accreditation badge"></div>
  <div class="badge badge--assoc-a" role="img" aria-label="Association membership badge"></div>
  <div class="badge badge--assoc-b" role="img" aria-label="Association membership badge"></div>
  <div class="badge badge--assoc-c" role="img" aria-label="Association membership badge"></div>
  <div class="badge badge--assoc-d" role="img" aria-label="Association membership badge"></div>
  <div class="badge badge--assoc-e" role="img" aria-label="Association membership badge"></div>

  <div class="abs mail-column">
    <div class="return-address">4389 Juniper<br>Ave #7<br>Waukesha,<br>WI 53947</div>
    <div class="indicia">
      <span>Presorted<br>Standard<br>U.S. Postage</span>
      <strong>PAID</strong>
      <span>PMX</span>
    </div>
    <div class="offer offer--fall">
      <div class="offer-amount">15% OFF</div>
      <div class="offer-name">FALL SPECIAL</div>
      <div class="offer-note">while openings are still available</div>
    </div>
    <div class="offer offer--winter">
      <div class="offer-amount">25% OFF</div>
      <div class="offer-name">WINTER SPECIAL</div>
      <div class="offer-note">December - February, Interior Only</div>
    </div>
  </div>

  <div class="abs cta-title">CALL OR EMAIL TODAY!</div>
  <div class="abs contact">
    262-555-0147<br>
    www.BrightCoatCrew.example<br>
    BrightCoatOffice@mail.example
  </div>
  <div class="abs consult">
    <div class="consult-free">FREE</div>
    <div class="consult-name">COLOR CONSULTATIONS</div>
    <div class="consult-note">with interior or exterior booked jobs</div>
  </div>
</section>

</body>
</html>
```